Plakat für Fensterbau-Meisterbetrieb
Zielgruppe
Wir sind ein Fensterbau-Meisterbetrieb und überwiegend in der Modernisierung, Restaurierung und Instandhaltung tätig. Unsere Zielgruppe sind in unserer Region alle die Interesse an neuen Fenstern/Haustüren usw. haben.
Aufgabenstellung
Gesucht wird ein Design für ein Gerüst-Plakat, die Maße sind in den Anhängen. Das Design sollte an dem Bestehenden Firmenlogo/Website angeglichen sein. Ein kurzer Werbespruch 'Fenster die begeistern!' sollte auf dem Plakat zu finden sein. Die Homepage, Adresse (Am Wiesenrain 7, 74219 Talbrunn) und ganz Wichtig das Firmenlogo sollte ebenfalls vertreten sein.
Ansonsten lassen wir uns gerne von Kreativen Vorschlägen überraschen. =)
Ein Briefbogen zur Orientierung ist ebenfalls im Anhang.
Nachtrag zu den Vorgaben:
Das Firmenlogo sollte der „eyecatcher“ sein und der Werbespruch eher Nebensache.
Schriftart: MavenPro / MavenRegular

```html
<!DOCTYPE html>
<html lang="de">
<head>
<meta charset="utf-8">
<title>Kranzmüller – Gerüstplakat</title>
<link href="https://fonts.googleapis.com/css2?family=Maven+Pro:wght@400;500;700;800&display=swap" rel="stylesheet">
<style>
  :root {
    --canvas-bg: #e6e6e4;
    --banner-bg: #f7f7f6;
    --ink-dark: #58585a;
    --ink-mid: #6a6a6c;
    --brand-green: #6cc24a;
    --band-green: #4fb03a;
    --deep-green: #1d7a3c;
    --glass-grey: #7b7b7d;
    --white: #ffffff;
  }
  * { margin: 0; padding: 0; box-sizing: border-box; }
  html, body {
    width: 1200px; height: 800px; overflow: hidden;
    background: var(--canvas-bg);
    font-family: "Maven Pro", sans-serif;
  }
  .banner {
    position: absolute; left: 219px; top: 10px;
    width: 810px; height: 830px;
    transform: scale(0.94); transform-origin: top left;
    background: var(--banner-bg);
    overflow: hidden;
    box-shadow: 0 2px 10px rgba(0,0,0,0.12);
  }
  .brand {
    position: absolute; right: 82px; top: 110px;
    display: flex; flex-direction: column; align-items: flex-end;
  }
  .brand-row {
    display: flex; align-items: center; gap: 18px;
  }
  .brand-mark {
    width: 46px; height: 46px; background: var(--brand-green);
  }
  .brand-name {
    font-size: 66px; font-weight: 700; color: var(--ink-dark);
    letter-spacing: 1px; line-height: 1;
  }
  .brand-tagline {
    margin-top: 18px;
    font-size: 27px; font-weight: 500; color: var(--ink-mid);
    letter-spacing: 3.2px; line-height: 1;
  }
  .headline {
    position: absolute; left: 55px; top: 295px;
    font-size: 70px; font-weight: 800; color: var(--ink-dark);
    line-height: 1;
  }
  .subline {
    position: absolute; left: 55px; top: 378px;
    font-size: 42px; font-weight: 800; color: var(--brand-green);
    line-height: 1; letter-spacing: 0.5px;
  }
  .facade-art { position: absolute; left: 0; top: 0; width: 810px; height: 830px; }
  .address {
    position: absolute; right: 38px; top: 644px;
    text-align: right; color: var(--white);
    font-size: 28px; font-weight: 700; line-height: 1.27;
  }
  .web-band {
    position: absolute; left: 0; bottom: 0; width: 100%; height: 82px;
    background: var(--band-green);
    display: flex; align-items: center; justify-content: center;
    color: var(--white); font-size: 22px; font-weight: 500;
    letter-spacing: 0.3px;
  }
</style>
</head>
<body>
  <div class="banner">
    <svg class="facade-art" viewBox="0 0 810 830">
      <defs>
        <linearGradient id="glass" x1="0" y1="1" x2="1" y2="0">
          <stop offset="0" stop-color="#5cc04a"/>
          <stop offset="0.45" stop-color="#2f9a4a"/>
          <stop offset="0.75" stop-color="#1d7a3c"/>
          <stop offset="1" stop-color="#8fd06a"/>
        </linearGradient>
      </defs>
      <polygon points="410,525 610,322 682,322 480,525" fill="var(--glass-grey)"/>
      <polygon role="img" aria-label="Grüne Glasfassade eines modernen Gebäudes"
               points="118,748 395,525 560,525 745,322 810,322 810,748" fill="url(#glass)"/>
    </svg>

    <div class="brand">
      <div class="brand-row">
        <span class="brand-mark"></span>
        <span class="brand-name">Kranzmüller</span>
      </div>
      <div class="brand-tagline">GLAS- UND FENSTERTECHNIK</div>
    </div>

    <div class="headline">FENSTER</div>
    <div class="subline">DIE BEGEISTERN!</div>

    <div class="address">Am Wiesenrain 7<br>74219 Talbrunn</div>

    <div class="web-band">www.kranzmueller-fenstertechnik.de</div>
  </div>
</body>
</html>
```